English and Spanish Language School Needs a Business Card

Need a business card design a startup company called Corvelle Language School. The company will offer English and Spanish conversational level courses designed to make the learner feel comfortable with grammar and vocabulary. We would like to see a logo with some colour that should communicate learning, growth.

Target Market(s)

Consumers and businesses

Industry/Entity Type

Education

Contact Information for Business Card

TBD

Font styles to use
Serif

Requirements
Must have
• Include the following
• Logo
• Name
• Title
• Cellphone Number
• Office Phone number
• Email address
• Office Address

```html
<!DOCTYPE html>
<html lang="en">
<head>
<meta charset="utf-8">
<title>Corvelle Language School — Business Card</title>
<link rel="stylesheet" href="https://fonts.googleapis.com/css2?family=Jost:wght@400;500;600&display=swap">
<style>
  :root {
    --bg: #ece4d6;
    --teal: #3d8f99;
    --charcoal: #2f2f31;
    --red: #a42f2f;
    --white: #f4f2ee;
    --light: #d9d9d9;
  }
  html, body {
    margin: 0;
    padding: 0;
    width: 1200px;
    height: 840px;
    overflow: hidden;
    background: var(--bg);
    font-family: "Jost", sans-serif;
  }
  .canvas {
    position: relative;
    width: 1200px;
    height: 840px;
  }
  .card {
    position: absolute;
    top: 170px;
    width: 500px;
    height: 500px;
  }
  .card--back { left: 70px; }
  .card--front { left: 630px; }
  .card-shape {
    position: absolute;
    inset: 0;
    width: 500px;
    height: 500px;
  }
  .card-frame { fill: var(--teal); }
  .card-face--back { fill: var(--charcoal); }
  .card-face--front { fill: var(--red); }

  .contact {
    position: absolute;
    left: 40px;
    top: 120px;
    width: 400px;
    text-align: center;
    color: var(--light);
  }
  .contact-name {
    margin: 0;
    color: var(--teal);
    font-size: 27px;
    font-weight: 600;
    letter-spacing: 2px;
    text-transform: uppercase;
  }
  .contact-title {
    margin: 2px 0 0;
    font-size: 19px;
    font-weight: 400;
  }
  .contact-rule {
    width: 170px;
    height: 2px;
    margin: 12px auto 14px;
    background: var(--teal);
    border: 0;
  }
  .contact-lines {
    margin: 0;
    font-size: 17px;
    line-height: 1.45;
    letter-spacing: 0.5px;
  }

  .brand {
    position: absolute;
    left: 60px;
    top: 185px;
    width: 380px;
    text-align: center;
    color: var(--white);
  }
  .brand-name {
    margin: 0;
    font-size: 78px;
    font-weight: 500;
    line-height: 1;
    letter-spacing: -1px;
  }
  .brand-tagline {
    margin: 6px 0 0;
    font-size: 20px;
    font-weight: 400;
    letter-spacing: 1px;
  }
</style>
</head>
<body>
<main class="canvas">

  <section class="card card--back" aria-label="Card back with contact details">
    <svg class="card-shape" viewBox="0 0 500 500" aria-hidden="true">
      <path class="card-frame" d="M470 235 L470 480 L320 480 L320 452 A235 235 0 1 1 470 235 Z"/>
      <path class="card-face--back" d="M438 240 L438 448 L340 448 L340 418 A198 198 0 1 1 438 240 Z"/>
    </svg>
    <div class="contact">
      <h1 class="contact-name">Mara Lindqvist</h1>
      <p class="contact-title">General Manager</p>
      <hr class="contact-rule">
      <p class="contact-lines">
        48 Harbor Lane, Suite 305<br>
        Ashford MA 01820<br>
        M: 555-310-2048 · T: 555-310-2049<br>
        E: info@corvellelc.com<br>
        www.corvellelc.com
      </p>
    </div>
  </section>

  <section class="card card--front" aria-label="Card front with school name">
    <svg class="card-shape" viewBox="0 0 500 500" aria-hidden="true">
      <g transform="rotate(180 250 250)">
        <path class="card-frame" d="M470 235 L470 480 L320 480 L320 452 A235 235 0 1 1 470 235 Z"/>
        <path class="card-face--front" d="M438 240 L438 448 L340 448 L340 418 A198 198 0 1 1 438 240 Z"/>
      </g>
    </svg>
    <div class="brand">
      <p class="brand-name">corvelle</p>
      <p class="brand-tagline">Language School</p>
    </div>
  </section>

</main>
</body>
</html>
```